Bref créative
Logo for a homebuyer business
Brightkey Dwellings Homebuyers
Use same font as used in my logo
Miriam Colby
Co-Owner
xxxxx
BrightKeyDwellings@mailbox-example.net
BrightKeyDwellings.example

```html
<!DOCTYPE html>
<html lang="en">
<head>
<meta charset="utf-8">
<title>Brightkey Dwellings Homebuyers – Stationery</title>
<link rel="stylesheet" href="https://fonts.googleapis.com/css2?family=Cormorant+Garamond:wght@500;600&family=Open+Sans:ital,wght@0,400;0,600;1,600&display=swap">
<style>
  :root{
    --blue:#2f3b93;
    --brown:#9a6a3e;
    --paper:#ffffff;
    --stage:#e7e7e8;
    --ink:#4a4a55;
    --faint:#e3e5ef;
  }
  *{box-sizing:border-box;margin:0;padding:0}
  html,body{width:1200px;height:936px;overflow:hidden;background:var(--stage)}
  .canvas{position:relative;width:1200px;height:936px;font-family:"Open Sans",Arial,sans-serif;color:var(--ink)}
  .item{position:absolute;box-shadow:0 2px 6px rgba(0,0,0,.18)}
  .framed{padding:7px}
  .framed .sheet{width:100%;height:100%;background:var(--paper);position:relative}
  .brand{font-family:"Cormorant Garamond",Georgia,serif;font-weight:600;color:var(--blue);text-transform:uppercase;letter-spacing:.04em;line-height:1.05;display:flex;align-items:center;gap:6px}
  .brand .mark{width:.55em;height:.55em;background:var(--blue);flex:none}
  .small{font-size:7px;line-height:1.6;color:var(--ink)}
  .web{font-style:italic;font-weight:600;color:var(--blue);letter-spacing:.06em}

  /* Letterhead */
  .letterhead{left:182px;top:66px;width:385px;height:547px;background:linear-gradient(90deg,var(--blue) 0 70%,var(--brown) 70% 100%)}
  .letterhead .brand{position:absolute;left:20px;top:28px;font-size:15px}
  .letterhead .contact{position:absolute;right:22px;top:26px;text-align:left}
  .letterhead .watermark{position:absolute;left:0;right:0;top:190px;text-align:center;font-family:"Cormorant Garamond",Georgia,serif;font-weight:600;font-size:40px;color:var(--faint);text-transform:uppercase;letter-spacing:.05em;line-height:1.05}
  .letterhead .web{position:absolute;right:22px;bottom:16px;font-size:8px}

  /* Folder cover */
  .cover{left:633px;top:40px;width:385px;height:575px;background:linear-gradient(90deg,var(--blue) 0 59%,var(--brown) 59% 100%)}
  .cover .brand{position:absolute;left:0;right:0;top:205px;justify-content:center;font-size:26px;text-align:center}
  .cover .web{position:absolute;right:22px;bottom:16px;font-size:12px}

  /* Business cards */
  .card{width:178px;height:99px}
  .card-front{left:40px;top:655px;background:linear-gradient(90deg,var(--blue) 0 55%,var(--brown) 55% 100%);padding:4px}
  .card-front .brand{position:absolute;left:10px;top:22px;font-size:9px;width:70px}
  .card-front .person{position:absolute;left:92px;top:18px;font-size:6px;line-height:1.6}
  .card-front .person strong{color:var(--blue);font-weight:600}
  .card-back{left:40px;top:779px;background:linear-gradient(90deg,var(--brown) 0 50%,var(--brown) 50% 100%);padding:4px}
  .card-back .brand{position:absolute;left:10px;top:28px;font-size:10px}
  .card-back .web{position:absolute;left:10px;bottom:12px;font-size:6px}

  /* Envelopes */
  .envelope-front{left:268px;top:668px;width:423px;height:208px;background:linear-gradient(90deg,var(--blue) 0 62%,var(--brown) 62% 100%)}
  .envelope-front .brand{position:absolute;left:22px;top:26px;font-size:14px}
  .envelope-front .return{position:absolute;left:22px;top:66px}
  .envelope-back{left:736px;top:668px;width:421px;height:208px;background:var(--paper)}
  .envelope-back svg{position:absolute;inset:0}
  .envelope-back .brand{position:absolute;left:0;right:0;top:22px;justify-content:center;font-size:13px}
  .envelope-back .web{position:absolute;left:0;right:0;top:50px;text-align:center;font-size:7px}
</style>
</head>
<body>
<main class="canvas">

  <section class="item letterhead framed" aria-label="Letterhead">
    <div class="sheet">
      <div class="brand"><span class="mark"></span>Brightkey<br>Dwellings</div>
      <div class="contact small">
        P.O. Box 4410 Ridgefield, NY 10900<br>
        (555) 014-2287<br>
        BrightKeyDwellings@mailbox-example.net
      </div>
      <div class="watermark" aria-hidden="true">Brightkey<br>Dwellings</div>
      <div class="web">www.BrightKeyDwellings.example</div>
    </div>
  </section>

  <section class="item cover framed" aria-label="Folder cover">
    <div class="sheet">
      <div class="brand"><span class="mark"></span>Brightkey Dwellings</div>
      <div class="web">www.BrightKeyDwellings.example</div>
    </div>
  </section>

  <section class="item card card-front" aria-label="Business card front">
    <div class="sheet" style="background:var(--paper);width:100%;height:100%;position:relative">
      <div class="brand">Brightkey<br>Dwellings</div>
      <div class="person">
        <strong>Miriam Colby</strong><br>
        Co-Owner<br>
        (555) 014-2287<br>
        BrightKeyDwellings@<br>mailbox-example.net
      </div>
    </div>
  </section>

  <section class="item card card-back" aria-label="Business card back">
    <div style="background:var(--paper);width:100%;height:100%;position:relative">
      <div class="brand">Brightkey Dwellings</div>
      <div class="web">www.BrightKeyDwellings.example</div>
    </div>
  </section>

  <section class="item envelope-front framed" aria-label="Envelope front">
    <div class="sheet">
      <div class="brand"><span class="mark"></span>Brightkey Dwellings</div>
      <div class="return small">P.O. Box 4410 Ridgefield, NY 10900</div>
    </div>
  </section>

  <section class="item envelope-back" aria-label="Envelope back">
    <svg width="421" height="208" viewBox="0 0 421 208" aria-hidden="true">
      <polyline points="0,70 210,118 421,70" fill="none" stroke="#d8d8dc" stroke-width="1.2"/>
      <line x1="0" y1="208" x2="170" y2="110" stroke="#e4e4e7" stroke-width="1"/>
      <line x1="421" y1="208" x2="250" y2="110" stroke="#e4e4e7" stroke-width="1"/>
    </svg>
    <div class="brand">Brightkey Dwellings</div>
    <div class="web">www.BrightKeyDwellings.example</div>
  </section>

</main>
</body>
</html>
```